Frost Leaf: CBD and Herbal Topical Pain product needs a brochure

We need a brochure that educates customers on the product. The product combines traditional Chinese herbs used for pain and swelling with a strong dose of CBD to apply topical with a glass, roll-on applicator. We would like to see dark blue as a dominant color or anything ice related. The logo is an iceberg but doesn't need to be included.

Target Market(s)

Cannabis Dispensaries, Chiro, Acu offices,
Health / Wellness, Alternative Medicine

Industry/Entity Type

Alternative Medicine

Colors
0455a3

Requirements
Must have
• Frost Leaf
• 500mg CBD in 1oz
• For: Muscle, Joint Pain, Swelling, Acute Injuries, Chronic Pain, Arthritis
• Directions: Apply a thin layer of herbal formula over the affected area. Apply as needed.
• Caution: Avoid hot water shortly after application.
• Ingredients: Angelica Root, Camphor, Cannabidoil (CBD), Cinnamon, Dandelion, Gardenia, Ginger, Licorice, Menthol, Myrrh, Phellodendron Bark, Rhubarb, Safflower, Sesame Oil, Scutellaria
• Highlight amount of CBD: 500mg
• Secondary highlights it includes Turmeric and Magnesium
• Easy Roll-On Topical Pain Relief for Muscle Spasms, Joint Pain, Strains, Sprains, Swelling
• Increases circulation to increase recovery time. Great for athletes
• Stops pain by numbing painful, slower deep nerve signals by stimulating the faster, superficial nerves with a cooling sensation
• Reduce painful swelling and heat involved with inflammation.
• Breaks up damaged tissue to enhance the natural healing process
• Ingredients
• Dang Gui – Angelica : reduces swelling, generates tissue, alleviates pain, expels pus
• Cinnamon –Gui Zhi decreases arthritic pain
• Carthamus Flower / safflower –Hong Hua - reduces swelling, alleviates pain,
• Rhubarb – Da Huang -bruising, acute and chronic swelling
• Licorice –Gan Cao - alleviates spasms, anti-inflammatory
• Phellodendron Huang Bai– reduces swelling and pain
• Dandelion – Pu Gong Ying – reduces swelling and nodules, anti-inflammatory
• Mo Yao – Myrrh – reduces swelling, pain, bruising, and masses, promotes healing
• Ginger – Gan Jiang – chronic swelling, increases circulation
• Gardenia – Zhi Zi- Reduces swelling from trauma, bruising
• Scutellaria – Huang Qin – hot sores, swelling,
• Magnesium – helps muscle spasms
• Camphor – mild, local anesthetic effect, alleviates pain, pain and swelling from sprains
• Menthol – rashes, swelling, relaxes muscles
• Turmeric – reduces inflammation and swelling
• Sesame Oil – carrier oil
• Cannabidiol (CBD) Isolate
• Colloidal Silver (Natural Preservative)
• Formulated by a Herbalist and Doctor of Chinese Medicine, Dr. Wendell Prasky, DAOM
Nice to have
• Iceberg or ice theme
• Copy:
• Frost Leaf blends traditional Chinese herbs with a potent dose of hemp derived cannabidiol (CBD) isolate. Instantly feel the cooling icy sensation penetrate deep into sore muscles and joints to sooth away pain.
• Not only does the menthol give a temporary cooling effect which helps numb pain, the other herbal ingredients continue to soothe tight, achy muscles and joints. It can also be applied for an acute sprain or strain to reduce swelling, just like applying ice.
• Ice is used by athletes and recommended by doctors to reduce pain and swelling. Frost Leaf can reduce pain and swelling without having to carry a bag of ice around.
• With the easy roll-on application, you dont even have to get your hands cold!
• Traditional Chinese Medicine has used the same herbs for thousands of years to help ease the pain of injuries during battle. Herbal plasters, liniments, and oils were the most common application to maximize the healing benefits of the herbs. Frost Leaf uses organic, raw herbs which are ground into a fine powder and further extracted in sesame oil. Once extracted, the oil is filtered and then CBD is then added as the oil is cooling.
• Pictures of a few of the herbs - I have a few already if needed

```html
<!DOCTYPE html>
<html lang="en">
<head>
<meta charset="utf-8">
<title>Frost Leaf Brochure</title>
<link href="https://fonts.googleapis.com/css2?family=Lato:wght@400;700&display=swap" rel="stylesheet">
<style>
:root{
  --brand-blue:#0455a3;
  --deep-navy:#2c2942;
  --ink:#5a5a5a;
  --ink-dark:#222;
  --paper:#ffffff;
  --backdrop:#f4f4f4;
}
*{box-sizing:border-box;margin:0;padding:0}
html,body{width:1200px;height:1200px;overflow:hidden;background:var(--backdrop)}
body{position:relative;font-family:'Lato',sans-serif;color:var(--ink)}
.sheet{position:absolute;left:240px;width:871px;height:616px;transform:scale(.8);transform-origin:0 0;background:var(--paper);overflow:hidden;box-shadow:0 10px 30px rgba(0,0,0,.18)}
.sheet--inside{top:100px}
.sheet--outside{top:650px}
.block{position:absolute}
ul{list-style:none}
.dots li{position:relative;padding-left:16px;font-size:11px;line-height:14px;margin-bottom:13px}
.dots li::before{content:"";position:absolute;left:0;top:3px;width:7px;height:7px;border-radius:50%;background:var(--brand-blue)}

/* inside: intro panel */
.intro{left:0;top:0;width:289px;height:333px;padding:45px 0 0 17px}
.intro__title{font-size:36px;font-weight:700;color:var(--brand-blue);line-height:42px}
.intro__dose{font-size:18px;font-weight:700;color:var(--ink-dark);margin:8px 0 14px 1px}
.intro .dots{width:265px}
.photo{position:absolute}
.photo--drinks{left:289px;top:0;width:291px;height:333px;background:linear-gradient(160deg,#dfe9c8 0%,#b9d08c 30%,#c9304a 60%,#e7a07a 85%,#c8dbb0 100%)}
.photo--tea{left:0;top:333px;width:190px;height:283px;background:linear-gradient(170deg,#f3f1ec 0%,#ebe6dd 45%,#eba043 65%,#f2dfc8 90%)}
.highlights{left:190px;top:333px;width:390px;height:283px;background:var(--brand-blue);padding:18px 8px 0 16px;color:#fff}
.highlights__title{font-size:19px;font-weight:700;margin-bottom:13px}
.highlights .dots li{color:#fff;margin-bottom:13px}
.highlights .dots li::before{background:#fff}
.ingredients{left:580px;top:0;width:291px;height:616px}
.ingredients__bar{height:15px;background:var(--brand-blue)}
.ingredients .dots{padding:76px 6px 0 10px}
.ingredients .dots li{margin-bottom:5px;font-size:10.6px;line-height:13.5px}
.ingredients b{color:var(--ink-dark);font-weight:700}

/* outside */
.photo--herbs{left:0;top:0;width:871px;height:363px;background:radial-gradient(ellipse at 70% 45%,#e8e6e0 0%,#b8c4a6 22%,#4f7a3a 38%,#b37a3f 62%,#8a5528 100%)}
.wave{position:absolute;left:0;top:0}
.story{left:18px;top:100px;width:268px}
.story .dots li{font-size:12px;line-height:15px;margin-bottom:15px}
.story .dots li::before{top:4px;width:9px;height:9px}
.curve-clear{float:right;width:72px;height:45px}
.curve-clear--low{clear:right;width:34px;height:30px}
.contact{left:289px;top:378px;width:291px;text-align:center;color:#fff;font-size:12px;line-height:15px}
.mark{position:absolute;color:#fff;text-align:center;font-family:'Lato',sans-serif}
.mark__name{font-weight:700}
.mark__square{display:block;margin:0 auto;background:#fff}
.mark--small{left:289px;top:478px;width:291px}
.mark--small .mark__name{font-size:13px}
.mark--small .mark__square{width:22px;height:22px;margin:10px auto 8px}
.mark--small .mark__sub{font-size:8px;font-weight:700}
.mark--small .mark__tiny{font-size:5px}
.back-panel{left:580px;top:363px;width:291px;height:253px;background:var(--paper)}
.label{left:646px;top:384px;width:160px;height:185px;background:var(--deep-navy);padding-top:6px}
.label .mark__name{font-size:22px}
.label .mark__square{width:46px;height:46px;margin:24px auto 26px}
.label .mark__sub{font-size:15px}
.label .mark__tiny{font-size:8px;margin-top:3px}
.label .mark__size{font-size:10px;margin-top:5px}
.footer-bar{position:absolute;top:595px;height:21px;background:var(--brand-blue)}
</style>
</head>
<body>

<section class="sheet sheet--inside">
  <div class="block intro">
    <h1 class="intro__title">Frost Leaf</h1>
    <p class="intro__dose">500mg CBD in 1oz</p>
    <ul class="dots">
      <li>For: Muscle, Joint Pain, Swelling, Acute Injuries, Chronic Pain, Arthritis</li>
      <li>Directions: Apply a thin layer of herbal formula over the affected area. Apply as needed.</li>
      <li>Caution: Avoid hot water shortly after application.</li>
      <li>Ingredients: Angelica Root, Camphor, Cannabidoil (CBD), Cinnamon, Dandelion, Gardenia, Ginger, Licorice, Menthol, Myrrh, Phellodendron Bark, Rhubarb, Safflower, Sesame Oil, Scutellaria</li>
    </ul>
  </div>
  <div class="photo photo--drinks" role="img" aria-label="Two glasses of red herbal drink garnished with mint and flowers"></div>
  <div class="photo photo--tea" role="img" aria-label="Glasses of iced orange herbal tea with ginger and berries"></div>
  <div class="block highlights">
    <h2 class="highlights__title">Highlight amount of CBD: 500mg</h2>
    <ul class="dots">
      <li>Secondary highlights it includes Turmeric and Magnesium</li>
      <li>Easy Roll-On Topical Pain Relief for Muscle Spasms, Joint Pain, Strains, Sprains, Swelling</li>
      <li>Increases circulation to increase recovery time. Great for athletes</li>
      <li>Stops pain by numbing painful, slower deep nerve signals by stimulating the faster, superficial nerves with a cooling sensation</li>
      <li>Reduce painful swelling and heat involved with inflammation.</li>
      <li>Breaks up damaged tissue to enhance the natural healing process</li>
      <li>Ingredients</li>
    </ul>
  </div>
  <div class="block ingredients">
    <div class="ingredients__bar"></div>
    <ul class="dots">
      <li><b>Dang Gui</b> – Angelica : reduces swelling, generates tissue, alleviates pain, expels pus</li>
      <li><b>Cinnamon</b> –Gui Zhi decreases arthritic pain</li>
      <li><b>Carthamus Flower / safflower</b> –Hong Hua - reduces swelling, alleviates pain,</li>
      <li><b>Rhubarb</b> – Da Huang -bruising, acute and chronic swelling</li>
      <li><b>Licorice</b> –Gan Cao - alleviates spasms, anti-inflammatory</li>
      <li><b>Phellodendron Huang Bai</b>–reduces swelling and pain</li>
      <li><b>Dandelion</b> – Pu Gong Ying – reduces swelling and nodules, anti-inflammatory</li>
      <li><b>Mo Yao</b> – Myrrh – reduces swelling, pain, bruising, and masses, promotes healing</li>
      <li><b>Ginger</b> – Gan Jiang – chronic swelling, increases circulation</li>
      <li><b>Gardenia</b> – Zhi Zi- Reduces swelling from trauma, bruising</li>
      <li><b>Scutellaria</b> – Huang Qin – hot sores, swelling,</li>
      <li><b>Magnesium</b> – helps muscle spasms</li>
      <li><b>Camphor</b> – mild, local anesthetic effect, alleviates pain, pain and swelling from sprains</li>
      <li><b>Menthol</b> – rashes, swelling, relaxes muscles</li>
      <li><b>Turmeric</b> – reduces inflammation and swelling</li>
      <li><b>Sesame Oil</b> – carrier oil</li>
      <li>Cannabidiol (CBD) Isolate</li>
      <li>Colloidal Silver (Natural Preservative)</li>
      <li>Formulated by a Herbalist and Doctor of Chinese Medicine, Dr. Wendell Prasky, DAOM</li>
    </ul>
  </div>
</section>

<section class="sheet sheet--outside">
  <div class="photo photo--herbs" role="img" aria-label="Fresh green herbs with small purple flowers in a marble mortar and pestle on a wooden table"></div>
  <svg class="wave" width="871" height="616" viewBox="0 0 871 616" aria-hidden="true">
    <path d="M0,50 C120,20 230,60 290,150 C370,270 480,320 580,365 L580,616 L0,616 Z" fill="var(--deep-navy)"/>
    <path d="M0,50 C120,20 230,60 290,150 L290,616 L0,616 Z" fill="#fff"/>
    <path d="M0,44 C120,14 230,54 293,146 C373,266 480,316 582,360" fill="none" stroke="var(--brand-blue)" stroke-width="9"/>
  </svg>
  <div class="block story">
    <ul class="dots">
      <li><span class="curve-clear"></span><span class="curve-clear curve-clear--low"></span>Frost Leaf blends traditional Chinese herbs with a potent dose of hemp derived cannabidiol (CBD) isolate. Instantly feel the cooling icy sensation penetrate deep into sore muscles and joints to sooth away pain.</li>
      <li>Not only does the menthol give a temporary cooling effect which helps numb pain, the other herbal ingredients continue to soothe tight, achy muscles and joints. It can also be applied for an acute sprain or strain to reduce swelling, just like applying ice.</li>
      <li>Ice is used by athletes and recommended by doctors to reduce pain and swelling. Frost Leaf can reduce pain and swelling without having to carry a bag of ice around.</li>
      <li>With the easy roll-on application, you dont even have to get your hands cold!</li>
      <li>Traditional Chinese Medicine has used the same herbs for thousands of years to help ease the pain of injuries during battle. Herbal plasters, liniments, and oils were the most common application to maximize the healing benefits of the herbs. Frost Leaf uses organic, raw herbs which are ground into a fine powder</li>
    </ul>
  </div>
  <div class="block contact">
    <p>Adress: 12 Birch Lane, Northvale</p>
    <p>Phone: 555 014 2290</p>
    <p>Email: hello@frostleaf.example</p>
    <p>www.frostleaf.example</p>
  </div>
  <div class="mark mark--small">
    <p class="mark__name">Frost Leaf</p>
    <span class="mark__square"></span>
    <p class="mark__sub">Pain Relief</p>
    <p class="mark__tiny">Menthol, CBD, Turmeric &amp; Magnesium</p>
    <p class="mark__tiny">1 fl oz</p>
  </div>
  <div class="block back-panel"></div>
  <div class="mark label block">
    <p class="mark__name">Frost Leaf</p>
    <span class="mark__square"></span>
    <p class="mark__sub">Pain Relief</p>
    <p class="mark__tiny">Menthol, CBD, Turmeric &amp; Magnesium</p>
    <p class="mark__size">1 fl oz</p>
  </div>
  <div class="footer-bar" style="left:0;width:289px"></div>
  <div class="footer-bar" style="left:580px;width:291px"></div>
</section>

</body>
</html>
```